Bref créative
Logo for a homebuyer business
Brightkey Dwellings Homebuyers
Use same font as used in my logo
Miriam Colby
Co-Owner
xxxxx
BrightKeyDwellings@mailbox-example.net
BrightKeyDwellings.example

```html
<!DOCTYPE html>
<html lang="en">
<head>
<meta charset="utf-8">
<title>Brightkey Dwellings Homebuyers — Business Card</title>
<link rel="stylesheet" href="https://fonts.googleapis.com/css2?family=Open+Sans:wght@400;600&display=swap">
<style>
  :root {
    --backdrop: #e4e5e7;
    --navy: #2a3a93;
    --royal: #2f3fa8;
    --copper: #a76a3c;
    --ink: #3b3f4a;
    --muted: #6b7080;
    --paper: #ffffff;
    --rule: #c9ccd4;
  }
  * { box-sizing: border-box; margin: 0; padding: 0; }
  html, body {
    width: 1200px; height: 895px; overflow: hidden;
    background: var(--backdrop);
  }
  .canvas {
    width: 1200px; height: 895px;
    display: flex; flex-direction: column;
    align-items: center; justify-content: center; gap: 40px;
  }
  .card {
    width: 680px; height: 389px;
    padding: 18px;
    box-shadow: 0 6px 18px rgba(0,0,0,.12);
  }
  .card--back { background: var(--copper); padding: 10px; }
  .card--front { background: var(--royal); }
  .card__face {
    width: 100%; height: 100%;
    background: var(--paper);
    display: flex; align-items: center;
  }
  .card--back .card__face { flex-direction: column; justify-content: center; gap: 30px; }

  .brand { display: flex; flex-direction: column; align-items: center; gap: 12px; }
  .brand__mark { width: 20px; height: 20px; background: var(--navy); }
  .brand__name {
    font-family: "Open Sans", sans-serif; font-weight: 600;
    color: var(--navy); text-align: center;
    font-size: 24px; line-height: 1.25;
    max-width: 260px;
  }

  .website-line {
    font-family: "Open Sans", sans-serif; font-weight: 600;
    font-size: 15px; color: var(--navy);
  }

  .card--front .brand { width: 44%; }
  .card--front .brand__name { font-size: 21px; max-width: 230px; }
  .divider { width: 1px; height: 58%; background: var(--rule); flex: none; }
  .contact {
    padding-left: 22px;
    font-family: "Open Sans", sans-serif; color: var(--ink);
  }
  .contact__name { font-weight: 600; font-size: 18px; color: var(--royal); }
  .contact__role { font-size: 13.5px; color: var(--muted); margin-bottom: 16px; }
  .contact__list { list-style: none; display: flex; flex-direction: column; gap: 7px; }
  .contact__item { display: flex; align-items: center; gap: 8px; font-size: 13px; white-space: nowrap; }
  .contact__icon { width: 15px; height: 15px; flex: none; }
</style>
</head>
<body>
<main class="canvas">
  <section class="card card--back" aria-label="Card back">
    <div class="card__face">
      <div class="brand">
        <div class="brand__mark"></div>
        <div class="brand__name">Brightkey Dwellings Homebuyers</div>
      </div>
      <p class="website-line">www.BrightKeyDwellings.example</p>
    </div>
  </section>

  <section class="card card--front" aria-label="Card front">
    <div class="card__face">
      <div class="brand">
        <div class="brand__mark"></div>
        <div class="brand__name">Brightkey Dwellings Homebuyers</div>
      </div>
      <div class="divider"></div>
      <div class="contact">
        <p class="contact__name">Miriam Colby</p>
        <p class="contact__role">Co-Owner</p>
        <ul class="contact__list">
          <li class="contact__item">
            <svg class="contact__icon" viewBox="0 0 16 16"><circle cx="8" cy="8" r="8" fill="#3b3f4a"/><path d="M5.2 4.2l1.4-.3.8 1.9-.9.7c.5 1.1 1.3 1.9 2.4 2.4l.7-.9 1.9.8-.3 1.4c-3.4.1-6.2-2.7-6-6z" fill="#fff"/></svg>
            123-456-7890
          </li>
          <li class="contact__item">
            <svg class="contact__icon" viewBox="0 0 16 16"><circle cx="8" cy="8" r="8" fill="#3b3f4a"/><rect x="5.5" y="3.5" width="5" height="9" rx="1" fill="#fff"/><rect x="6.3" y="4.6" width="3.4" height="5.8" fill="#3b3f4a"/></svg>
            (555) 014-2236
          </li>
          <li class="contact__item">
            <svg class="contact__icon" viewBox="0 0 16 16"><circle cx="8" cy="8" r="8" fill="#3b3f4a"/><rect x="4" y="5" width="8" height="6" fill="#fff"/><path d="M4 5l4 3.2L12 5" stroke="#3b3f4a" stroke-width="1" fill="none"/></svg>
            BrightKeyDwellings@mailbox-example.net
          </li>
          <li class="contact__item">
            <svg class="contact__icon" viewBox="0 0 16 16"><circle cx="8" cy="8" r="8" fill="#3b3f4a"/><circle cx="8" cy="8" r="4.2" fill="none" stroke="#fff" stroke-width="1"/><ellipse cx="8" cy="8" rx="1.8" ry="4.2" fill="none" stroke="#fff" stroke-width="1"/><path d="M3.8 8h8.4" stroke="#fff" stroke-width="1"/></svg>
            www.BrightKeyDwellings.example
          </li>
        </ul>
      </div>
    </div>
  </section>
</main>
</body>
</html>
```